New Logo, New Business Cards! Looking for Refresh

We're in the process of modernizing our entire organization, and with that came the redesign of our logo (attached). We're looking for a designer to develop our new business cards.
Looking for a design that will bring the company in 2020 and help showcase our new logo. Work with the colors of the logo. Feel free to experiment with the logo in white or black if you want. Both now attached.
Industry/Entity Type
Non Profit
Contact Information for Business Card
Address:
48315 Brackwell Avenue, Suite 512
Richmond Hill, ON, L7R 5K2
Name: Marcus Delvecki, MBA
Position: Executive Director
Telephone: 905-362-7048, Ext. 218
Cell Phone: 416-573-2046
Email: marcus@quorvel.ca
Website: www.quorvel.ca
Look and feel
Each slider illustrates characteristics of the customer's brand and the style your logo design should communicate.

```html
<!DOCTYPE html>
<html lang="en">
<head>
<meta charset="utf-8">
<title>Quorvel Business Cards</title>
<link href="https://fonts.googleapis.com/css2?family=Lato:wght@400;700;900&display=swap" rel="stylesheet">
<style>
  :root {
    --bg: #9b9b9b;
    --green-dark: #0e3b22;
    --green-mid: #0f4426;
    --green-bright: #4a9a3f;
    --card-light: #e4e4e4;
    --swoosh: #f4f4f4;
    --text: #4a4a4a;
    --white: #ffffff;
  }
  * { margin: 0; padding: 0; box-sizing: border-box; }
  html, body { width: 1200px; height: 900px; overflow: hidden; }
  body {
    background: var(--bg);
    font-family: "Lato", sans-serif;
    position: relative;
  }
  .card {
    position: absolute;
    left: 363px;
    width: 474px;
    height: 271px;
    overflow: hidden;
  }
  .card--front {
    top: 145px;
    background: linear-gradient(135deg, var(--green-mid), var(--green-dark));
    display: flex;
    align-items: center;
    justify-content: center;
  }
  .brand-name {
    font-family: "Lato", sans-serif;
    font-weight: 900;
    letter-spacing: 2px;
  }
  .card--front .brand-name {
    color: var(--white);
    font-size: 46px;
  }
  .card--back {
    top: 484px;
    background: var(--card-light);
  }
  .card--back .brand-name {
    position: absolute;
    left: 25px;
    top: 36px;
    color: var(--green-dark);
    font-size: 36px;
  }
  .person {
    position: absolute;
    right: 26px;
    top: 112px;
    text-align: right;
  }
  .person__name {
    font-weight: 700;
    font-size: 14px;
    color: var(--green-dark);
  }
  .person__title {
    font-size: 11px;
    color: var(--text);
    margin-top: 4px;
  }
  .rule {
    position: absolute;
    left: 27px;
    top: 141px;
    width: 322px;
    height: 1.5px;
    background: var(--green-bright);
  }
  .contacts {
    position: absolute;
    left: 26px;
    top: 157px;
    list-style: none;
    font-size: 11px;
    color: var(--text);
    line-height: 15px;
  }
  .contacts li { display: flex; align-items: center; gap: 5px; }
  .contacts svg { width: 9px; height: 9px; fill: var(--green-bright); flex: none; }
  .ext { color: var(--green-bright); }
  .address {
    position: absolute;
    left: 26px;
    top: 215px;
    font-style: normal;
    font-size: 11px;
    line-height: 15px;
    color: var(--text);
  }
  .footer-shape {
    position: absolute;
    left: 0;
    bottom: 0;
    width: 474px;
    height: 27px;
  }
  .website {
    position: absolute;
    right: 26px;
    bottom: 9px;
    font-size: 10.5px;
    color: var(--white);
  }
</style>
</head>
<body>
  <section class="card card--front">
    <span class="brand-name">QUORVEL</span>
  </section>

  <section class="card card--back">
    <span class="brand-name">QUORVEL</span>

    <div class="person">
      <p class="person__name">Marcus Delvecki, MBA</p>
      <p class="person__title">Executive Director</p>
    </div>
    <div class="rule"></div>

    <ul class="contacts">
      <li>
        <svg viewBox="0 0 10 10"><path d="M2.5 0h5a1 1 0 0 1 1 1v8a1 1 0 0 1-1 1h-5a1 1 0 0 1-1-1V1a1 1 0 0 1 1-1zm.5 1.2v6.6h4V1.2z"/></svg>
        416-573-2046
      </li>
      <li>
        <svg viewBox="0 0 10 10"><path d="M2 0.5l1.8 2.2-1 1.1c.7 1.5 1.9 2.7 3.4 3.4l1.1-1L9.5 8 8.4 9.4C4.5 9.4.6 5.5.6 1.6z"/></svg>
        <span>905-362-7048, <span class="ext">Ext.</span> 218</span>
      </li>
      <li>
        <svg viewBox="0 0 10 10"><path d="M0 2h10v6H0zm.8.6L5 5.6l4.2-3z"/></svg>
        marcus@quorvel.ca
      </li>
    </ul>

    <address class="address">
      48315 Brackwell Avenue, Suite 512<br>
      Richmond Hill, ON, L7R 5K2
    </address>

    <svg class="footer-shape" viewBox="0 0 474 27" preserveAspectRatio="none">
      <rect x="0" y="13" width="474" height="14" fill="var(--green-dark)"/>
      <path d="M296 13 H330 C340 18 352 27 370 27 H336 C320 27 308 18 296 13 Z" fill="var(--swoosh)"/>
      <path d="M302 0 H474 V27 H352 C334 27 322 8 302 0 Z" fill="var(--green-bright)"/>
    </svg>
    <span class="website">www.quorvel.ca</span>
  </section>
</body>
</html>
```